Stationery Design Project for Lotvian, Chicago

Lotvian, a street parking application which helps car drivers find a street parking spot by offering an ideal path along which to look for parking. This path is calculated by our algorithm based on data (e.g. historical data, baseball games schedule, etc.). Along this path the driver will find a spot and will also save 70% of the search time. Customer we target is reg. between 21 and 45 yo.

We envision something young, fresh, bright and original. Slightly abstract maybe. It should represent the idea and elements of finding street parking in the city, e.g. car(s), parking spot, people, city, etc. (just ideas!).

Requirement:
- Business Cards (2 Sided Full Color CMYK)
- Letterhead (1 Sided Full Color CMYK)
- Envelope (1 Sided Full Color CMYK)
- Sticker (1 Sided Full Color CMYK), round with a 2inch diameter.

Reason: We're starting to get more and more designs and need more time to look into all of them. Very exciting!! Thanks to everybody!

Hi all, we're in the process of selecting our favs. Though choices!!! Really good submissions. Will keep you posted and sorry for the delay.

Target Market(s)

Car drivers and owners between 21 and 45

Industry/Entity Type

Parking

Requirements
Must have
• Sticker should be round and include company URL lotvian.com and the new logo which we will attach soon.
Should not have
• Should not be too serious or boring.

```html
<!DOCTYPE html>
<html lang="en">
<head>
<meta charset="utf-8">
<title>Lotvian — Business Card</title>
<link rel="stylesheet" href="https://fonts.googleapis.com/css2?family=Open+Sans:wght@400;600;700&family=Play:wght@400;700&display=swap">
<style>
  :root {
    --page: #d9d6d0;
    --card: #f1f1f0;
    --ink: #232323;
    --ink-soft: #4a4a4a;
    --rule: #3a3a3a;
    --brand-blue: #1c4fb3;
    --path-blue: #b7d0ea;
  }
  * { box-sizing: border-box; margin: 0; padding: 0; }
  html, body { width: 1200px; height: 720px; overflow: hidden; }
  body {
    background: var(--page);
    font-family: "Open Sans", Arial, sans-serif;
    color: var(--ink);
    position: relative;
  }
  .card {
    position: absolute;
    top: 205px;
    width: 540px;
    height: 309px;
    background: var(--card);
    box-shadow: 0 2px 6px rgba(0,0,0,.18);
    overflow: hidden;
  }
  .card--front { left: 40px; }
  .card--back { left: 620px; }

  /* front */
  .brand {
    position: absolute;
    left: 32px; top: 30px;
    display: flex; align-items: center; gap: 16px;
  }
  .brand__dot {
    width: 58px; height: 58px; border-radius: 50%;
    background: var(--brand-blue);
  }
  .brand__name {
    font-family: "Open Sans", Arial, sans-serif;
    font-weight: 700;
    font-size: 42px;
    color: var(--ink);
    letter-spacing: .5px;
  }
  .rule-main {
    position: absolute; left: 32px; right: 32px; top: 112px;
    border-top: 1.5px solid var(--rule);
  }
  .person { position: absolute; left: 32px; top: 126px; }
  .person__name { font-weight: 700; font-size: 20px; color: var(--ink); }
  .person__role { font-size: 14px; color: var(--ink-soft); margin-top: 1px; }
  .rule-short {
    position: absolute; left: 32px; width: 222px; top: 186px;
    border-top: 1px solid var(--rule);
  }
  .contact { position: absolute; left: 32px; top: 200px; list-style: none; }
  .contact li {
    display: flex; align-items: center; gap: 14px;
    font-size: 14px; color: var(--ink-soft); height: 26px;
  }
  .contact svg { width: 14px; height: 14px; fill: var(--ink); flex: none; }
  .address {
    position: absolute; left: 326px; top: 126px;
    font-size: 12.5px; line-height: 26px; color: var(--ink-soft);
  }

  /* back */
  .path-art {
    position: absolute; left: 60px; top: 40px; width: 420px; height: 240px;
    background: linear-gradient(135deg, rgba(183,208,234,.55), rgba(183,208,234,.25));
  }
  .back-brand {
    position: absolute; left: 0; right: 0; top: 62px;
    display: flex; flex-direction: column; align-items: center; gap: 10px;
  }
  .back-brand__dot {
    width: 76px; height: 76px; border-radius: 50%;
    background: var(--brand-blue);
  }
  .back-brand__name {
    font-family: "Open Sans", Arial, sans-serif;
    font-weight: 700; font-size: 22px; color: var(--ink);
  }
  .tagline {
    position: absolute; left: 0; right: 0; top: 200px;
    text-align: center;
    font-family: "Play", Arial, sans-serif;
    font-size: 22px; color: var(--ink); letter-spacing: .3px;
  }
</style>
</head>
<body>

<section class="card card--front">
  <div class="brand">
    <span class="brand__dot"></span>
    <span class="brand__name">lotvian</span>
  </div>
  <div class="rule-main"></div>

  <div class="person">
    <p class="person__name">Maren Tol Vesting</p>
    <p class="person__role">Director</p>
  </div>
  <div class="rule-short"></div>

  <ul class="contact">
    <li>
      <svg viewBox="0 0 14 14" aria-hidden="true"><path d="M4 0h6a1 1 0 0 1 1 1v12a1 1 0 0 1-1 1H4a1 1 0 0 1-1-1V1a1 1 0 0 1 1-1zm.5 2v7h5V2z"/></svg>
      +31 612 480 375
    </li>
    <li>
      <svg viewBox="0 0 14 14" aria-hidden="true"><path d="M0 3h14v9H0zm1.3 1 5.7 4 5.7-4v-.1H1.3zm0 1.3V11h11.4V5.3L7 9.3z"/></svg>
      maren@lotvian.com
    </li>
    <li>
      <svg viewBox="0 0 14 14" aria-hidden="true"><path d="M7 1 0 7h2v6h4V9h2v4h4V7h2z"/></svg>
      www.lotvian.com
    </li>
  </ul>

  <p class="address">North Wells 2046, Loop district,<br>Chicago, USA</p>
</section>

<section class="card card--back">
  <div class="path-art" role="img" aria-label="Abstract light blue street path lines forming a parking route"></div>
  <div class="back-brand">
    <span class="back-brand__dot"></span>
    <span class="back-brand__name">lotvian</span>
  </div>
  <p class="tagline">Find Your Spot Faster</p>
</section>

</body>
</html>
```